Real Estate Listing Signs for standard Yard arms

I need real estate listing signs done, for the standard sized sign to be hung beneath a white yard arm. To match existing logo. Information to be included:
-Logo
-Business name
-Phone number
-Marden Fosk Tundra Circle & Marden Fosk Realty logos (smaller print)

Colors to be Red and anywhere in the gray scale between black and white, or a combination of those.

Target Market(s)

Drive by visuals

Industry/Entity Type

Real Estate Agent

Colors

Designer to choose only greyscale colors for use in the design.

Requirements
Must have
• My Logo and business name in same/similar font to whats provided, the MF tundra circle logo (small on bottom or corner somewhere), My phone number, and a decent amount of red coloration on the sign.

```html
<!DOCTYPE html>
<html lang="en">
<head>
<meta charset="utf-8">
<title>Listing Sign Concepts – Brantley Realty</title>
<link rel="stylesheet" href="https://fonts.googleapis.com/css2?family=Archivo+Black&family=Montserrat:wght@500;800;900&family=Roboto+Condensed:wght@400;500&display=swap">
<style>
  :root {
    --red: #ff0a1e;
    --black: #000000;
    --white: #ffffff;
    --canvas: #ebebeb;
    --ink: #333333;
  }
  * { box-sizing: border-box; margin: 0; padding: 0; }
  html, body { width: 1200px; height: 639px; overflow: hidden; }
  body {
    background: var(--canvas);
    position: relative;
    font-family: "Montserrat", sans-serif;
  }
  .page-title {
    position: absolute; top: 40px; left: 0; width: 1200px;
    text-align: center; font-weight: 500; font-size: 26px;
    color: var(--ink); letter-spacing: 0.3px;
  }
  .sample-label {
    position: absolute; top: 577px;
    font-weight: 500; font-size: 17px; color: var(--ink);
  }
  .sign {
    position: absolute; top: 117px; width: 337px; height: 433px;
    background: var(--black); overflow: hidden;
  }
  .sign--one { left: 43px; background: linear-gradient(var(--red) 0 230px, var(--black) 230px); }
  .sign--two { left: 424px; }
  .sign--three { left: 805px; background: var(--red); }
  .side-stripes {
    position: absolute; top: 36px; width: 8px; height: 230px;
    background: repeating-linear-gradient(var(--black) 0 22px, var(--red) 22px 38px);
  }
  .side-stripes--left { left: 0; }
  .side-stripes--right { right: 0; }
  .panel {
    position: absolute; left: 8px; right: 8px; top: 10px; height: 373px;
    background: var(--white); overflow: hidden;
  }
  .footer-band { position: absolute; left: 0; right: 0; top: 383px; bottom: 0; background: var(--black); }
  .brand-mark {
    position: absolute; left: 50%; top: 38px; width: 96px; height: 96px;
    margin-left: -48px; background: var(--red);
  }
  .brand-name {
    position: absolute; left: 0; right: 0; top: 170px;
    text-align: center; font-family: "Archivo Black", sans-serif;
    font-size: 33px; line-height: 33px; letter-spacing: 1px; color: var(--black);
  }
  .agent-name {
    position: absolute; left: 0; right: 0; top: 269px; text-align: center;
    font-weight: 900; font-size: 19px; line-height: 20px; color: var(--black);
  }
  .agent-rule {
    position: absolute; top: 281px; height: 3px; width: 40px; background: var(--black);
  }
  .agent-rule--left { left: 0; }
  .agent-rule--right { right: 0; }
  .phone {
    position: absolute; left: 0; right: 0; top: 297px; text-align: center;
    font-weight: 900; font-size: 41px; line-height: 44px; color: var(--red); letter-spacing: -0.5px;
  }
  .email {
    position: absolute; left: 0; right: 0; top: 345px; text-align: center;
    font-weight: 900; font-size: 17px; line-height: 20px; color: var(--black);
  }
  .brokerage {
    position: absolute; left: 20px; top: 396px; color: var(--white);
    font-family: "Roboto Condensed", sans-serif; font-weight: 500;
  }
  .brokerage-name { font-size: 14px; line-height: 14px; text-transform: uppercase; letter-spacing: -0.2px; }
  .brokerage-sub { font-size: 6px; line-height: 8px; text-transform: uppercase; }
  .disclaimer {
    position: absolute; right: 21px; top: 397px; text-align: right; color: var(--white);
    font-size: 8.5px; font-weight: 500; line-height: 12px;
  }
  /* sample two */
  .sign--two .panel { height: 377px; }
  .sign--two .footer-band { top: 387px; }
  .sign--two .brokerage { top: 398px; }
  .sign--two .disclaimer { top: 398px; }
  .sign--two .curve { position: absolute; left: 0; top: 231px; width: 321px; height: 80px; }
  .sign--two .agent-name { top: 274px; color: var(--white); }
  .sign--two .phone-band { position: absolute; left: 0; right: 0; top: 301px; height: 51px; background: var(--black); }
  .sign--two .phone { top: 303px; }
  .sign--two .email-band { position: absolute; left: 0; right: 0; top: 352px; height: 25px; background: var(--red); }
  .sign--two .email { top: 353px; color: var(--white); }
  /* sample three */
  .sign--three .footer-band { background: var(--black); }
  .sign--three .agent-name { top: 267px; }
  .sign--three .agent-rule { background: var(--red); top: 281px; }
  .sign--three .phone-band { position: absolute; left: 0; right: 0; top: 295px; height: 50px; background: var(--red); }
  .sign--three .phone { color: var(--white); top: 297px; }
  .sign--three .email { top: 348px; }
</style>
</head>
<body>
  <h1 class="page-title">Real Estate Listing Signs for standard Yard arms</h1>

  <section class="sign sign--one">
    <div class="footer-band"></div>
    <div class="panel">
      <div class="brand-mark"></div>
      <div class="brand-name">BRANTLEY<br>REALTY</div>
      <div class="agent-rule agent-rule--left"></div>
      <div class="agent-rule agent-rule--right"></div>
      <div class="agent-name">JORDAN BRANTLEY</div>
      <div class="phone">907-555-0148</div>
      <div class="email">JBRANTLEY@MAIL.COM</div>
    </div>
    <div class="brokerage"><div class="brokerage-name">MF tundra circle</div><div class="brokerage-sub">Marden Fosk Realty</div></div>
    <div class="disclaimer">Each Offce Independently<br>Owned and operated</div>
  </section>

  <section class="sign sign--two">
    <div class="footer-band"></div>
    <div class="panel">
      <div class="brand-mark"></div>
      <div class="brand-name">BRANTLEY<br>REALTY</div>
      <svg class="curve" viewBox="0 0 321 80" preserveAspectRatio="none" aria-hidden="true">
        <path d="M0 5 Q160 75 321 0 L321 80 L0 80 Z" fill="#ff0a1e"/>
      </svg>
      <div class="agent-name">JORDAN BRANTLEY</div>
      <div class="phone-band"></div>
      <div class="phone">907-555-0148</div>
      <div class="email-band"></div>
      <div class="email">JBRANTLEY@MAIL.COM</div>
    </div>
    <div class="brokerage"><div class="brokerage-name">MF tundra circle</div><div class="brokerage-sub">Marden Fosk Realty</div></div>
    <div class="disclaimer">Each Offce Independently<br>Owned and operated</div>
  </section>

  <section class="sign sign--three">
    <div class="side-stripes side-stripes--left"></div>
    <div class="side-stripes side-stripes--right"></div>
    <div class="footer-band"></div>
    <div class="panel">
      <div class="brand-mark"></div>
      <div class="brand-name">BRANTLEY<br>REALTY</div>
      <div class="agent-rule agent-rule--left"></div>
      <div class="agent-rule agent-rule--right"></div>
      <div class="agent-name">JORDAN BRANTLEY</div>
      <div class="phone-band"></div>
      <div class="phone">907-555-0148</div>
      <div class="email">JBRANTLEY@MAIL.COM</div>
    </div>
    <div class="brokerage"><div class="brokerage-name">MF tundra circle</div><div class="brokerage-sub">Marden Fosk Realty</div></div>
    <div class="disclaimer">Each Offce Independently<br>Owned and operated</div>
  </section>

  <p class="sample-label" style="left:43px">Sample 1</p>
  <p class="sample-label" style="left:419px">Sample 2</p>
  <p class="sample-label" style="left:805px">Sample 3</p>
</body>
</html>
```